Poster of Insipirational Quotes

Attached is a list of leadership quotes from Harold Brenwick. I would like a poster made, incorporating whatever design elements you like, potentially including Harold's face, and one or more of the quotes. I intend to print this out in A3 or larger to hang on my wall.

The quotes are:

Being responsible sometimes means pissing people off.

The day soldiers stop bringing you their problems is the day you have stopped leading them.

Don't be buffaloed by experts and elites. Experts often possess more data than judgment. Elites can become so inbred that they produce hemophiliacs who bleed to death as soon as they are nicked by the real world.

Don't be afraid to challenge the pros, even in their own backyard.

Never neglect details. When everyone's mind is dulled or distracted the leader must be doubly vigilant.

You don't know what you can get away with until you try.

Keep looking below surface appearances. Don't shrink from doing so (just) because you might not like what you find.

Organization doesn't really accomplish anything. Plans don't accomplish anything, either. Theories of management don't much matter. Endeavors succeed or fail because of the people involved. Only by attracting the best people will you accomplish great deeds.

Organization charts and fancy titles count for next to nothing.

Never let your ego get so close to your position that when your position goes, your ego goes with it.

Fit no stereotypes. Don't chase the latest management fads. The situation dictates which approach best accomplishes the team's mission.

Perpetual optimism is a force multiplier.

Look for intelligence and judgment, and most critically, a capacity to anticipate, to see around corners. Also look for loyalty, integrity, a high energy drive, a balanced ego, and the drive to get things done.

Great leaders are almost always great simplifiers, who can cut through argument, debate and doubt, to offer a solution everybody can understand.

The commander in the field is always right and the rear echelon is wrong, unless proved otherwise.

Have fun in your command. Don't always run at a breakneck pace. Take leave when you've earned it: Spend time with your families. Corollary: surround yourself with people who take their work seriously, but not themselves, those who work hard and play hard.

Command is lonely.

Leadership is the art of accomplishing more than the science of management
says is possible.

I need to modify the specification based on the designs that I've seen.

Executive Office

Designer to choose colors to be used in the design.

• Quotes

```html
<!DOCTYPE html>
<html lang="en">
<head>
<meta charset="utf-8">
<title>Leadership Quote Cards</title>
<link href="https://fonts.googleapis.com/css2?family=Josefin+Sans:wght@400;600&display=swap" rel="stylesheet">
<style>
  :root {
    --board: #e6e6e6;
    --card: #ffffff;
    --ink: #111111;
    --shadow: rgba(0, 0, 0, 0.28);
    --line-art: #d9d9d9;
    --pencil: #b4b4b4;
    --engraving: #c3c3c3;
  }
  html, body {
    margin: 0;
    width: 1200px;
    height: 1200px;
    overflow: hidden;
    background: var(--board);
  }
  .board {
    position: relative;
    width: 1200px;
    height: 1200px;
  }
  .card {
    position: absolute;
    width: 481px;
    height: 340px;
    background: var(--card);
    box-shadow: 0 6px 14px var(--shadow);
    overflow: hidden;
  }
  .col-left { left: 74px; }
  .col-right { left: 646px; }
  .row-1 { top: 40px; }
  .row-2 { top: 430px; }
  .row-3 { top: 821px; }

  .portrait {
    position: absolute;
    left: 131px;
    top: 28px;
    width: 240px;
    height: 285px;
    border-radius: 120px 120px 10px 10px;
  }
  .portrait.line-art {
    background: linear-gradient(180deg, var(--line-art) 0%, #ececec 60%, rgba(255,255,255,0) 100%);
  }
  .portrait.pencil {
    left: 96px;
    top: 36px;
    width: 248px;
    height: 268px;
    background: linear-gradient(180deg, var(--pencil) 0%, #cfcfcf 65%, rgba(255,255,255,0) 100%);
  }
  .portrait.engraving {
    left: 131px;
    top: 30px;
    width: 242px;
    height: 305px;
    background: linear-gradient(180deg, var(--engraving) 0%, #d6d6d6 65%, rgba(255,255,255,0) 100%);
  }

  .quote-bold {
    position: absolute;
    left: 18px;
    top: 226px;
    margin: 0;
    color: var(--ink);
    font-family: "Josefin Sans", sans-serif;
    font-weight: 600;
  }
  .quote-bold .lead {
    display: block;
    font-size: 30px;
    letter-spacing: 4.6px;
    line-height: 38px;
  }
  .quote-bold .follow {
    display: block;
    font-size: 19px;
    letter-spacing: 3.1px;
    line-height: 24px;
  }

  .quote-long {
    position: absolute;
    left: 14px;
    top: 238px;
    width: 460px;
    margin: 0;
    color: var(--ink);
    font-family: "Josefin Sans", sans-serif;
    font-weight: 400;
    font-size: 12.6px;
    line-height: 15.2px;
    letter-spacing: 1.55px;
    white-space: pre;
  }
</style>
</head>
<body>
<main class="board">

  <section class="card col-left row-1">
    <div class="portrait line-art" role="img" aria-label="Line drawing portrait of a general in dress uniform"></div>
    <p class="quote-bold"><span class="lead">"Being responsible</span><span class="follow">sometimes means pissing people off."</span></p>
  </section>

  <section class="card col-right row-1">
    <div class="portrait line-art" role="img" aria-label="Line drawing portrait of a general in dress uniform"></div>
    <p class="quote-long">"The day soldiers stop bringing you their problems is the
day you have stopped leading them.  They have either lost
confidence that you can help them or concluded that you
do not care.  Either case is a failure of leadership."</p>
  </section>

  <section class="card col-left row-2">
    <div class="portrait pencil" role="img" aria-label="Pencil sketch portrait of a smiling man in glasses"></div>
    <p class="quote-bold"><span class="lead">"Being responsible</span><span class="follow">sometimes means pissing people off."</span></p>
  </section>

  <section class="card col-right row-2">
    <div class="portrait pencil" role="img" aria-label="Pencil sketch portrait of a smiling man in glasses"></div>
    <p class="quote-long">"The day soldiers stop bringing you their problems is the
day you have stopped leading them.  They have either lost
confidence that you can help them or concluded that you
do not care.  Either case is a failure of leadership."</p>
  </section>

  <section class="card col-left row-3">
    <div class="portrait engraving" role="img" aria-label="Engraved-style portrait of a general in uniform with medals"></div>
    <p class="quote-bold"><span class="lead">"Being responsible</span><span class="follow">sometimes means pissing people off."</span></p>
  </section>

  <section class="card col-right row-3">
    <div class="portrait engraving" role="img" aria-label="Engraved-style portrait of a general in uniform with medals"></div>
    <p class="quote-long">"The day soldiers stop bringing you their problems is the
day you have stopped leading them.  They have either lost
confidence that you can help them or concluded that you
do not care.  Either case is a failure of leadership."</p>
  </section>

</main>
</body>
</html>
```